依頼概要
◆概要・特徴
弊社はweb上で印刷を承る印刷通販を運営しております。
https://qorvaprint.example/
お客様が選んで使える「感染症対策ポスター」のデザイン作成をお願いいたします。

【当選内容】
複数当選(最大3点)を予定しておりますので、ご応募は1点ずつお願いいたします。
お一人様で何点でもご応募いただけます。

【デザインの要望】
・オフィス内、飲食内、旅館など様々な場所を想定しておりますので共通性・汎用性のあるデザインを宜しくお願いします。
イメージ画像を添付します。

【サイズ詳細】
作成サイズ A2トンボ付き

その他何かご不明な点がございましたら、お気軽にご質問下さい。
よろしくお願いいたします。
皆様、ご応募いただき誠にありがとうございます。
当選デザインについてはなるべくテイストが異なるものを選びたいと思っており、添付画像のような爽やかなカラフル感?も頂けると嬉しいです。
■ 選んだ理由

汎用性があるデザイン(オフィス内・飲食・etc)で清潔さがあるのをレギュラーとしながらも明るい感じのデザインも望んでおりました為、選ばせていただきました。

■ 提案者全員のお礼・コメント

大変よく出来たデザインばかりだったため、選ぶのに非常に悩んでおりました。
この度は貴重なデザインを応募頂き誠にありがとうございました。

```html
<!DOCTYPE html>
<html lang="ja">
<head>
<meta charset="UTF-8">
<title>新型コロナ感染対策 実施中</title>
<link rel="stylesheet" href="https://fonts.googleapis.com/css2?family=M+PLUS+Rounded+1c:wght@700;800;900&family=Mochiy+Pop+One&display=swap">
<style>
  :root {
    --sky-top: #a9dcf2;
    --sky-mid: #d6effa;
    --sky-low: #eef8fc;
    --grass: #9fd36a;
    --grass-deep: #7cbf4a;
    --title-green: #1f9a7a;
    --pink: #f0709a;
    --pink-soft: #fde3ec;
    --blue: #5fb6e6;
    --blue-soft: #e1f2fb;
    --green: #78c04a;
    --green-soft: #e7f5dc;
    --orange: #f29a2e;
    --orange-soft: #fdebd3;
    --yellow: #f3c531;
    --yellow-soft: #fff6d2;
    --teal: #63c1a8;
    --teal-soft: #ddf3ec;
    --purple: #a47fc9;
    --purple-soft: #efe6f8;
    --arrow-red: #e5302f;
    --white: #ffffff;
  }
  * { box-sizing: border-box; margin: 0; padding: 0; }
  html, body { width: 853px; height: 1200px; overflow: hidden; background: var(--white); }
  .poster {
    position: relative;
    width: 853px;
    height: 1200px;
    overflow: hidden;
    font-family: "M PLUS Rounded 1c", sans-serif;
  }
  .scenery {
    position: absolute;
    inset: 0;
    background:
      radial-gradient(ellipse 140px 260px at 30px 330px, #8fcf6a 0%, #8fcf6a 60%, transparent 62%),
      radial-gradient(ellipse 140px 260px at 823px 330px, #8fcf6a 0%, #8fcf6a 60%, transparent 62%),
      radial-gradient(ellipse 520px 200px at 200px 930px, var(--grass) 0%, var(--grass) 70%, transparent 72%),
      radial-gradient(ellipse 560px 220px at 680px 960px, var(--grass-deep) 0%, var(--grass-deep) 70%, transparent 72%),
      linear-gradient(180deg, var(--sky-top) 0%, var(--sky-mid) 35%, var(--sky-low) 70%, var(--grass) 82%, var(--grass-deep) 100%);
  }
  .heading {
    position: absolute;
    top: 34px;
    left: 0;
    width: 100%;
    text-align: center;
  }
  .heading-sub {
    font-weight: 900;
    font-size: 46px;
    letter-spacing: 3px;
    color: var(--title-green);
    -webkit-text-stroke: 9px var(--white);
    paint-order: stroke fill;
  }
  .heading-main {
    margin-top: 4px;
    font-family: "Mochiy Pop One", sans-serif;
    font-size: 118px;
    line-height: 1.1;
    letter-spacing: 28px;
    padding-left: 28px;
    color: var(--pink);
    -webkit-text-stroke: 14px var(--white);
    paint-order: stroke fill;
  }
  .measures {
    position: absolute;
    top: 250px;
    left: 60px;
    width: 733px;
    display: grid;
    grid-template-columns: repeat(3, 1fr);
    grid-template-rows: 205px 193px 240px;
    column-gap: 18px;
    row-gap: 30px;
  }
  .card {
    --c: var(--pink);
    --soft: var(--pink-soft);
    background: var(--white);
    border: 5px solid var(--c);
    border-radius: 6px;
    padding: 8px;
    display: flex;
    flex-direction: column;
    gap: 8px;
  }
  .card--wide { grid-column: span 2; }
  .card--pink { --c: var(--pink); --soft: var(--pink-soft); }
  .card--blue { --c: var(--blue); --soft: var(--blue-soft); }
  .card--green { --c: var(--green); --soft: var(--green-soft); }
  .card--orange { --c: var(--orange); --soft: var(--orange-soft); }
  .card--yellow { --c: var(--yellow); --soft: var(--yellow-soft); }
  .card--teal { --c: var(--teal); --soft: var(--teal-soft); }
  .card--purple { --c: var(--purple); --soft: var(--purple-soft); }
  .card-art {
    flex: 1;
    border-radius: 4px;
    background: radial-gradient(circle at 50% 45%, var(--soft) 0%, var(--white) 85%);
  }
  .card-label {
    border: 3px solid var(--c);
    border-radius: 4px;
    background: var(--white);
    color: var(--c);
    font-weight: 800;
    font-size: 17px;
    line-height: 1.3;
    text-align: center;
    padding: 5px 4px;
  }
  .card-label--inline { align-self: flex-start; width: 58%; }
  .distance-scene {
    flex: 1;
    display: flex;
    align-items: center;
    gap: 10px;
  }
  .distance-figure {
    width: 110px;
    height: 100%;
    border-radius: 4px;
    background: radial-gradient(circle at 50% 45%, var(--soft) 0%, var(--white) 85%);
  }
  .distance-arrow { flex: 1; height: 40px; }
  .card--split { flex-direction: row; }
  .card--split .card-art { flex: 1; }
  .split-side { width: 55%; display: flex; flex-direction: column; justify-content: flex-end; gap: 8px; }
  .thanks {
    position: absolute;
    top: 1078px;
    left: 0;
    width: 100%;
    text-align: center;
    font-weight: 900;
    font-size: 40px;
    letter-spacing: 2px;
    color: var(--pink);
    -webkit-text-stroke: 9px var(--white);
    paint-order: stroke fill;
  }
</style>
</head>
<body>
<main class="poster">
  <div class="scenery" role="img" aria-label="青空と雲、左右の木々、風船、手前の草原の背景イラスト"></div>

  <header class="heading">
    <h1 class="heading-sub">新型コロナ感染対策</h1>
    <p class="heading-main">実施中</p>
  </header>

  <section class="measures">
    <article class="card card--pink">
      <div class="card-art" role="img" aria-label="マスクをつけたうさぎのイラスト"></div>
      <p class="card-label">マスクを<br>つけています</p>
    </article>
    <article class="card card--blue">
      <div class="card-art" role="img" aria-label="窓を開けて換気するねこのイラスト"></div>
      <p class="card-label">定期的に<br>換気しています</p>
    </article>
    <article class="card card--green">
      <div class="card-art" role="img" aria-label="手洗いをするうさぎのイラスト"></div>
      <p class="card-label">こまめに手洗いを<br>しています</p>
    </article>

    <article class="card card--orange">
      <div class="card-art" role="img" aria-label="消毒液を差し出す犬のイラスト"></div>
      <p class="card-label">除菌消毒に<br>ご協力ください</p>
    </article>
    <article class="card card--yellow card--wide">
      <div class="distance-scene">
        <div class="distance-figure" role="img" aria-label="距離をとるねこのイラスト"></div>
        <svg class="distance-arrow" viewBox="0 0 200 40" preserveAspectRatio="none" aria-hidden="true">
          <polygon points="0,20 26,2 26,13 174,13 174,2 200,20 174,38 174,27 26,27 26,38" fill="var(--arrow-red)"/>
        </svg>
        <div class="distance-figure" role="img" aria-label="距離をとるもう一匹のねこのイラスト"></div>
      </div>
      <p class="card-label">適切な距離をとって<br>施設をご利用ください</p>
    </article>

    <article class="card card--teal card--wide card--split">
      <div class="card-art" role="img" aria-label="飛沫防止シート越しのうしとライオンのイラスト"></div>
      <div class="split-side">
        <p class="card-label">飛沫防止シートや間仕切りで<br>「密」にならないようにしています</p>
      </div>
    </article>
    <article class="card card--purple">
      <div class="card-art" role="img" aria-label="消毒スプレーを持つくまのイラスト"></div>
      <p class="card-label">施設内を<br>消毒しています</p>
    </article>
  </section>

  <p class="thanks">ご協力ありがとうございます</p>
</main>
</body>
</html>
```